Eye-catching Card for new church

I would like a card the size of a business card ... that can be used to announce the start of our new church. I would like it to have our logo on the card, my name, and the statement "Coming Soon ... 1.10.2016". I also would like to list our website address and Facebook page and my Twitter account.

Target Market(s)

prospective people looking for a church

Industry/Entity Type

Church

Requirements
Must have
• a focus on Coming Soon ... 1.10.2016
• Brightfold Church logo
Should not have
• church buildings or writings on the cross

```html
<!DOCTYPE html>
<html lang="en">
<head>
<meta charset="utf-8">
<title>Brightfold Church – Coming Soon Card</title>
<link rel="stylesheet" href="https://fonts.googleapis.com/css2?family=Great+Vibes&family=Cormorant+Garamond:wght@500&family=Crimson+Text:wght@400;600&display=swap">
<style>
  :root {
    --backdrop: #e4e4e6;
    --card-dark: #1b1b1d;
    --card-mid: #2c2c2f;
    --card-edge: #3a3a3e;
    --text-light: #f2f2f2;
    --text-soft: #d6d6d8;
    --rule: #6d6d72;
    --accent-blue: #3f86e0;
    --accent-blue-soft: #5aa2f0;
  }
  * { margin: 0; padding: 0; box-sizing: border-box; }
  html, body {
    width: 1200px;
    height: 1000px;
    overflow: hidden;
    background: var(--backdrop);
  }
  .stage {
    width: 1200px;
    height: 1000px;
    display: flex;
    align-items: center;
    justify-content: center;
  }
  .card {
    position: relative;
    width: 1000px;
    height: 572px;
    border-radius: 6px;
    overflow: hidden;
    box-shadow: 0 10px 30px rgba(0,0,0,0.25);
  }
  .card__texture {
    position: absolute;
    inset: 0;
    background: radial-gradient(ellipse at 40% 35%, var(--card-mid) 0%, var(--card-dark) 70%);
  }
  .card__texture::after {
    content: "";
    position: absolute;
    inset: 0;
    background: linear-gradient(135deg, rgba(255,255,255,0.03) 0%, rgba(0,0,0,0.15) 100%);
  }

  /* Announcement */
  .announcement {
    position: absolute;
    left: 120px;
    top: 95px;
    width: 420px;
    text-align: center;
    color: var(--text-light);
  }
  .flourish-row {
    display: flex;
    align-items: center;
    justify-content: center;
    gap: 14px;
    height: 40px;
  }
  .flourish-row__rule {
    width: 70px;
    height: 1px;
    background: var(--rule);
  }
  .flourish {
    width: 56px;
    height: 34px;
    border-radius: 17px;
    background: radial-gradient(ellipse, rgba(90,162,240,0.55) 0%, rgba(63,134,224,0.15) 70%, transparent 100%);
  }
  .announcement__headline {
    font-family: "Great Vibes", cursive;
    font-size: 84px;
    line-height: 1.05;
    font-weight: 400;
    margin-top: 6px;
  }
  .announcement__date {
    font-family: "Crimson Text", serif;
    font-size: 38px;
    letter-spacing: 1px;
    margin: 4px 0 8px;
  }

  /* Name mark */
  .church-mark {
    position: absolute;
    right: 80px;
    top: 150px;
    width: 320px;
    text-align: center;
    color: var(--text-light);
    font-family: "Cormorant Garamond", serif;
    font-weight: 500;
  }
  .church-mark__square {
    width: 54px;
    height: 54px;
    background: var(--text-light);
    margin: 0 auto 22px;
  }
  .church-mark__name {
    font-size: 46px;
    letter-spacing: 7px;
    line-height: 1;
  }
  .church-mark__sub {
    font-size: 20px;
    letter-spacing: 12px;
    margin-top: 10px;
  }

  /* Contact */
  .contact {
    position: absolute;
    left: 60px;
    bottom: 48px;
    font-family: "Crimson Text", serif;
    color: var(--text-soft);
  }
  .contact__name {
    font-weight: 600;
    font-size: 34px;
    letter-spacing: 1px;
    color: var(--accent-blue);
    line-height: 1.1;
  }
  .contact__social {
    display: flex;
    gap: 28px;
    font-size: 22px;
    margin-top: 4px;
  }
  .contact__item {
    display: flex;
    align-items: center;
    gap: 9px;
  }
  .contact__dot {
    width: 12px;
    height: 12px;
    border-radius: 50%;
    background: var(--accent-blue-soft);
  }
  .contact__web {
    font-size: 22px;
    margin-top: 2px;
  }
</style>
</head>
<body>
<main class="stage">
  <article class="card">
    <div class="card__texture" role="img" aria-label="Dark charcoal low-poly faceted background pattern"></div>

    <section class="announcement">
      <div class="flourish-row">
        <span class="flourish-row__rule"></span>
        <span class="flourish" role="img" aria-label="Blue decorative swirl ornament"></span>
        <span class="flourish-row__rule"></span>
      </div>
      <h1 class="announcement__headline">Coming Soon ..</h1>
      <p class="announcement__date">1st-October-2016</p>
      <div class="flourish-row">
        <span class="flourish-row__rule"></span>
        <span class="flourish" role="img" aria-label="Blue decorative swirl ornament"></span>
        <span class="flourish-row__rule"></span>
      </div>
    </section>

    <section class="church-mark">
      <div class="church-mark__square"></div>
      <p class="church-mark__name">BRIGHTFOLD</p>
      <p class="church-mark__sub">CHURCH</p>
    </section>

    <section class="contact">
      <p class="contact__name">EVAN MARLOW</p>
      <div class="contact__social">
        <span class="contact__item"><span class="contact__dot"></span>@MarlowEv</span>
        <span class="contact__item"><span class="contact__dot"></span>/BrightfoldChurchFM.com</span>
      </div>
      <p class="contact__web">www.thebrightfoldchurch.com</p>
    </section>
  </article>
</main>
</body>
</html>
```